Professional Business Card for Luxury Hotel & Resort Development Firm. Advisory firm

Project Overview: We are a specialized advisory firm focused on Hotel & Resort Development. Our clients are high-net-worth investors and major hospitality brands.

Design Requirements:

Style: Minimalist, sophisticated, and trustworthy. We want to avoid looking too "corporate" or "dry"—it should feel premium.

Key Elements: Please incorporate our logo [もしロゴがあれば] and emphasize a clean layout with plenty of white space.

Color Palette: We prefer Grey and White or Black and White to evoke a sense of luxury and stability.

Typography: Professional garamond, or sans-serif or elegant serif fonts

Goal: The card should feel substantial and high-end when handed to a client, reflecting our expertise in multi-million dollar developments.
Updates

I am currently on a business trip for field research and have limited access to my desktop. Additionally, I have just provided detailed technical feedback to a designer and am waiting for their refined proposals. To ensure the final logo meets the high standards of my new advisory firm, I would like to extend the deadline by 7 days. Thank you for your support.

Target Market(s)

High-net-worth investors, luxury hospitality brands, and real estate developers.

Contact Information for Business Card

Firm Name: Harbor Crest Partners, My Name: Kenji Morisawa, Title: Founder, Address 5-8-4 Kitanomura Aoba Yokohama Japan 225-0143, email address: kmorisawa@harborcrestpx.example, Tel: +81 90-4183-2750. Front Site (Primary): Japanese translation of the back side, Please use a clean Japanese font (like Mincho) that complements the Garmond on the English side Back side: English. Note for Japanese text: since the frond side is the main fae, please ensure the layout is clean and professional. Please use a high-quality Mincho ( Serif-style) font for Japanese to mach the Garmond used on the English side. Text for Front side (Japanese) Harbor Crest Partners, 役職:代表、森沢健二、225-0143 横浜市青葉区北野村5-8-4. Name of the firm can stay in English.

Font styles to use
Other font styles liked:
• Font Preference: Please use Garamond for all text to maintain a consistent, elegant, and classic professional look.

Requirements
Must have
• Professional and clean layout, high-end feel.
Nice to have
• Minimalist design with subtle luxury accents.

```html
<!DOCTYPE html>
<html lang="en">
<head>
<meta charset="utf-8">
<title>Kenji Morisawa — Business Card</title>
<link rel="stylesheet" href="https://fonts.googleapis.com/css2?family=Manrope:wght@400;500;700&display=swap">
<style>
  :root {
    --page-bg: #e6e6e6;
    --card-bg: #060709;
    --bar-light: #6a6a6d;
    --bar-dark: #3d3d3f;
    --text-strong: #6e6e71;
    --text-soft: #77777a;
  }
  * { margin: 0; padding: 0; box-sizing: border-box; }
  html, body {
    width: 1200px;
    height: 1200px;
    overflow: hidden;
    background: var(--page-bg);
    font-family: "Manrope", sans-serif;
  }
  .card {
    position: absolute;
    left: 110px;
    top: 320px;
    width: 980px;
    height: 560px;
    background: var(--card-bg);
    overflow: hidden;
  }
  .accent-vertical {
    position: absolute;
    left: 797px;
    top: 0;
    width: 95px;
    height: 100%;
    background: var(--bar-light);
  }
  .accent-horizontal {
    position: absolute;
    left: 641px;
    top: 50px;
    width: 339px;
    height: 95px;
    background: var(--bar-dark);
  }
  .identity {
    position: absolute;
    left: 62px;
    top: 226px;
    white-space: nowrap;
    color: var(--text-strong);
  }
  .identity .name {
    font-size: 46px;
    font-weight: 700;
    letter-spacing: 0.2px;
  }
  .identity .title {
    font-size: 26px;
    font-weight: 400;
    color: var(--text-soft);
    margin-left: 6px;
  }
  .contact {
    position: absolute;
    left: 62px;
    top: 336px;
    list-style: none;
    color: var(--text-soft);
    font-size: 25px;
    line-height: 38.5px;
    letter-spacing: 0.3px;
  }
  .contact li {
    display: flex;
    align-items: flex-start;
  }
  .contact .icon {
    width: 22px;
    height: 22px;
    margin-top: 8px;
    margin-right: 25px;
    flex-shrink: 0;
    fill: var(--text-soft);
  }
  .contact .phone { font-weight: 700; color: var(--text-strong); }
</style>
</head>
<body>
  <section class="card" aria-label="Business card">
    <div class="accent-vertical"></div>
    <div class="accent-horizontal"></div>

    <h1 class="identity">
      <span class="name">Kenji Morisawa</span><span class="title">| Founder</span>
    </h1>

    <ul class="contact">
      <li>
        <svg class="icon" viewBox="0 0 24 24" aria-hidden="true">
          <path d="M6.6 10.8c1.4 2.8 3.8 5.1 6.6 6.6l2.2-2.2c.3-.3.7-.4 1-.2 1.1.4 2.3.6 3.6.6.6 0 1 .4 1 1V20c0 .6-.4 1-1 1C10.6 21 3 13.4 3 4c0-.6.4-1 1-1h3.5c.6 0 1 .4 1 1 0 1.3.2 2.5.6 3.6.1.3 0 .7-.2 1L6.6 10.8z"/>
          <path d="M15 3.5a6 6 0 0 1 5.5 5.5h-1.6A4.4 4.4 0 0 0 15 5.1zM15 6.6a3 3 0 0 1 2.4 2.4h-1.6a1.5 1.5 0 0 0-.8-.8z"/>
        </svg>
        <span class="phone">+81 90-4183-2750.</span>
      </li>
      <li>
        <svg class="icon" viewBox="0 0 24 24" aria-hidden="true">
          <path d="M3 5h18v14H3zM12 12.5 19.5 7h-15z" fill-rule="evenodd"/>
        </svg>
        <span>kmorisawa@harborcrestpx.example</span>
      </li>
      <li>
        <svg class="icon" viewBox="0 0 24 24" aria-hidden="true">
          <path d="M12 2a7 7 0 0 0-7 7c0 5.2 7 13 7 13s7-7.8 7-13a7 7 0 0 0-7-7zm0 9.5A2.5 2.5 0 1 1 12 6.5a2.5 2.5 0 0 1 0 5z"/>
        </svg>
        <span>5-8-4 Kitanomura Aoba Yokohama<br>Japan 225-0143</span>
      </li>
    </ul>
  </section>
</body>
</html>
```